School Hallway Magnetic Display Design for school values

I am looking for a someone to help me design a magnetic hallway display that will hang in the hallway of our small school. There are several elements, including 1. 6ft by 4ft designed magnetic bulletin board, 2. Magnets that will stick to the board. See attachment for which elements belong where. The display will be for our TRAVEK program, which rewards students for demonstrating our school values. We want the display to be beautiful and interactive. We are also rebranding, so we want the design to align with our new fonts and colors. In the attached PDF is an outline of our new brand guidelines. Unfortunately, we don't have the color codes, but I'm hoping that you can match the colors listed. Attached are elements to be used on the board, but please use your creativity to make it more dynamic and visually appealing. For example, the star magnets could be another shape. The TRAVEK magnets must remain the same. I've included two photos of boards at other schools that inspired this project.

Target Market(s)

School Community

Industry/Entity Type

Education

Requirements
Should not have
• School Logo

```html
<!DOCTYPE html>
<html lang="en">
<head>
<meta charset="utf-8">
<title>TRAVEK of the Month – Hallway Display</title>
<link rel="stylesheet" href="https://fonts.googleapis.com/css2?family=Roboto:wght@500;700;900&display=swap">
<style>
  :root {
    --page: #ffffff;
    --board: #ffffff;
    --ink: #1d4e5c;
    --teal: #1d8aa6;
    --blue: #2a8fc4;
    --sky: #8ccde0;
    --green: #7cbf5a;
    --leaf: #4f9f5a;
    --deep-green: #3b7d52;
    --yellow: #f0bf3a;
  }
  * { box-sizing: border-box; margin: 0; padding: 0; }
  html, body { width: 1200px; height: 1200px; overflow: hidden; background: var(--page); }
  body { position: relative; font-family: "Roboto", Arial, sans-serif; color: var(--ink); }

  .board {
    position: absolute; left: 59px; top: 225px; width: 1084px; height: 748px;
    background: var(--board);
    border: 1px solid #e3e6e6;
    box-shadow: 0 6px 14px rgba(0,0,0,0.12);
    overflow: hidden;
  }
  .corner-wash { position: absolute; opacity: .7; }
  .corner-wash--top-left { left: -120px; top: -120px; width: 520px; height: 520px; background: radial-gradient(circle, #dff0ea 0%, #eaf5f7 35%, rgba(255,255,255,0) 70%); }
  .corner-wash--bottom-right { right: -140px; bottom: -140px; width: 520px; height: 520px; background: radial-gradient(circle, #fbf0cc 0%, #e4f2f3 35%, rgba(255,255,255,0) 70%); }
  .corner-wash--bottom-left { left: -120px; bottom: -120px; width: 340px; height: 400px; background: radial-gradient(circle, #fbf1d2 0%, rgba(255,255,255,0) 70%); }

  .board-title {
    position: absolute; left: 0; top: 38px; width: 1030px; text-align: center;
    font-weight: 700; font-size: 52px; letter-spacing: -0.5px;
    color: var(--teal);
  }
  .board-title .joiner { position: relative; }
  .board-title .joiner::after {
    content: ""; position: absolute; left: 0; right: 0; bottom: -4px; height: 4px;
    background: var(--green); border-radius: 2px;
  }

  .value-card {
    position: absolute; width: 340px; height: 90px;
    background: #fff; border: 6px solid var(--card-border); border-radius: 10px;
    display: flex; align-items: center; justify-content: center; gap: 10px;
    font-weight: 700; font-size: 40px; color: var(--ink);
    overflow: hidden;
    box-shadow: 0 2px 4px rgba(0,0,0,0.12);
  }
  .value-card::before {
    content: ""; position: absolute; left: 0; top: 0; width: 72px; height: 100%;
    background: linear-gradient(160deg, var(--sky) 0%, var(--green) 55%, var(--leaf) 100%);
    clip-path: polygon(0 0, 55% 0, 100% 100%, 0 100%);
    opacity: .9;
  }
  .value-card::after {
    content: ""; position: absolute; right: 0; top: 0; width: 36px; height: 30px;
    background: var(--corner);
    clip-path: polygon(0 0, 100% 0, 100% 100%);
  }
  .value-card .icon { position: absolute; left: 14px; top: 50%; transform: translateY(-50%); width: 44px; height: 44px; z-index: 1; }
  .value-card .label { position: relative; z-index: 1; padding-left: 40px; }

  .value-card--simplicity { left: 66px; top: 170px; --card-border: var(--green); --corner: var(--teal); }
  .value-card--peace { left: 430px; top: 170px; --card-border: var(--blue); --corner: var(--yellow); }
  .value-card--integrity { left: 66px; top: 298px; --card-border: var(--teal); --corner: var(--green); }
  .value-card--community { left: 430px; top: 298px; --card-border: var(--green); --corner: var(--sky); }
  .value-card--equality { left: 66px; top: 420px; --card-border: var(--sky); --corner: var(--yellow); }
  .value-card--stewardship { left: 430px; top: 420px; --card-border: var(--leaf); --corner: var(--green); }
  .value-card--integrity::before, .value-card--community::before { background: linear-gradient(160deg, var(--yellow) 0%, var(--green) 60%, var(--leaf) 100%); }
  .value-card--equality::before { background: linear-gradient(160deg, var(--yellow) 0%, var(--yellow) 50%, var(--sky) 100%); }

  .thermometer { position: absolute; left: 740px; top: 30px; width: 300px; height: 710px; }
  .achievement-label {
    position: absolute; left: 953px; top: 131px; width: 110px;
    font-weight: 700; font-size: 12px; letter-spacing: .3px; color: var(--ink);
  }
  .magnet-tray { position: absolute; left: 120px; top: 540px; width: 600px; height: 160px; }
</style>
</head>
<body>
  <main class="board">
    <div class="corner-wash corner-wash--top-left" role="img" aria-label="Soft geometric line pattern in pale green, blue and yellow"></div>
    <div class="corner-wash corner-wash--bottom-left" role="img" aria-label="Soft geometric line pattern in pale yellow"></div>
    <div class="corner-wash corner-wash--bottom-right" role="img" aria-label="Soft geometric line pattern in pale blue and yellow"></div>

    <h1 class="board-title">TRAVEK <span class="joiner">of</span> the Month</h1>

    <div class="value-card value-card--simplicity">
      <svg class="icon" viewBox="0 0 44 44"><path d="M22 4 C34 12 34 32 22 40 C10 32 10 12 22 4Z" fill="#4f9f5a"/><path d="M22 10 V38" stroke="#fff" stroke-width="2"/></svg>
      <span class="label">Simplicity</span>
    </div>
    <div class="value-card value-card--peace">
      <svg class="icon" viewBox="0 0 44 44" role="img" aria-label="Dove of peace icon"><ellipse cx="22" cy="24" rx="18" ry="11" fill="#2a8fc4"/></svg>
      <span class="label">Peace</span>
    </div>
    <div class="value-card value-card--integrity">
      <svg class="icon" viewBox="0 0 44 44" role="img" aria-label="Handshake icon"><rect x="4" y="14" width="36" height="16" rx="8" fill="#2a8fc4"/></svg>
      <span class="label">Integrity</span>
    </div>
    <div class="value-card value-card--community">
      <svg class="icon" viewBox="0 0 44 44"><path d="M4 22 L22 6 L40 22 H35 V40 H9 V22Z" fill="#4f9f5a"/><rect x="18" y="27" width="8" height="13" fill="#fff"/></svg>
      <span class="label">Community</span>
    </div>
    <div class="value-card value-card--equality">
      <svg class="icon" viewBox="0 0 44 44" fill="none" stroke="#1d4e5c" stroke-width="2.5"><path d="M22 6 V38 M12 38 H32 M8 12 H36"/><path d="M8 12 L3 26 H13Z M36 12 L31 26 H41Z"/></svg>
      <span class="label">Equality</span>
    </div>
    <div class="value-card value-card--stewardship">
      <svg class="icon" viewBox="0 0 44 44"><circle cx="22" cy="17" r="14" fill="#7cbf5a"/><rect x="20" y="26" width="4" height="16" fill="#3b7d52"/></svg>
      <span class="label">Stewardship</span>
    </div>

    <svg class="thermometer" viewBox="0 0 300 710">
      <defs>
        <clipPath id="tube-clip">
          <rect x="118" y="32" width="76" height="560" rx="38"/>
          <circle cx="156" cy="600" r="78"/>
        </clipPath>
        <linearGradient id="bulb-fill" x1="0" y1="0" x2="1" y2="1">
          <stop offset="0" stop-color="#7cbf5a"/>
          <stop offset=".5" stop-color="#4fae7a"/>
          <stop offset="1" stop-color="#1d8aa6"/>
        </linearGradient>
      </defs>
      <path d="M156 20 A50 50 0 0 0 106 70 V522.8 A92 92 0 1 0 206 522.8 V70 A50 50 0 0 0 156 20Z" fill="#fff"/>
      <g clip-path="url(#tube-clip)">
        <rect x="100" y="0" width="120" height="710" fill="#eef3f4"/>
        <rect x="118" y="40" width="38" height="90" fill="#dde9ec"/>
        <rect x="100" y="130" width="56" height="100" fill="#7cbf5a"/>
        <rect x="156" y="130" width="60" height="100" fill="#4f9f5a"/>
        <rect x="100" y="230" width="56" height="100" fill="#2a8fc4"/>
        <rect x="156" y="230" width="60" height="100" fill="#1d7fae"/>
        <rect x="100" y="330" width="56" height="90" fill="#8ccde0"/>
        <rect x="156" y="330" width="60" height="90" fill="#5db6cc"/>
        <rect x="100" y="420" width="56" height="100" fill="#f0bf3a"/>
        <rect x="156" y="420" width="60" height="100" fill="#2a8fc4"/>
        <rect x="100" y="520" width="120" height="190" fill="url(#bulb-fill)"/>
      </g>
      <path d="M156 20 A50 50 0 0 0 106 70 V522.8 A92 92 0 0 0 156 692" fill="none" stroke="#7cbf5a" stroke-width="9"/>
      <path d="M156 20 A50 50 0 0 1 206 70 V522.8 A92 92 0 0 1 156 692" fill="none" stroke="#1d8aa6" stroke-width="9"/>
      <ellipse cx="128" cy="572" rx="14" ry="10" fill="#fff" opacity=".4"/>
      <g stroke="#1d4e5c" stroke-width="2.5">
        <line x1="216" y1="100" x2="228" y2="100"/><line x1="216" y1="122" x2="236" y2="122"/>
        <line x1="216" y1="144" x2="228" y2="144"/><line x1="216" y1="166" x2="228" y2="166"/>
        <line x1="216" y1="188" x2="236" y2="188"/><line x1="216" y1="210" x2="228" y2="210"/>
        <line x1="216" y1="232" x2="228" y2="232"/><line x1="216" y1="254" x2="236" y2="254"/>
        <line x1="216" y1="276" x2="228" y2="276"/><line x1="216" y1="298" x2="228" y2="298"/>
        <line x1="216" y1="320" x2="236" y2="320"/><line x1="216" y1="342" x2="228" y2="342"/>
        <line x1="216" y1="364" x2="228" y2="364"/><line x1="216" y1="386" x2="236" y2="386"/>
        <line x1="216" y1="408" x2="228" y2="408"/><line x1="216" y1="430" x2="228" y2="430"/>
        <line x1="216" y1="452" x2="236" y2="452"/>
      </g>
      <g transform="translate(267 66)"><circle r="12" fill="#4f9f5a"/><path d="M-7 10 L-10 24 L-3 19 M7 10 L10 24 L3 19" fill="#4f9f5a"/><path d="M-5 0 L-1 4 L6 -4" stroke="#fff" stroke-width="2.5" fill="none"/></g>
      <path transform="translate(267 143)" d="M0 -14 L3 -3 L14 0 L3 3 L0 14 L-3 3 L-14 0 L-3 -3Z" fill="#f0bf3a"/>
      <g transform="translate(267 218)"><circle r="12" fill="#7cbf5a"/><circle r="6" fill="#2a8fc4"/><path d="M-7 10 L-10 24 L-3 19 M7 10 L10 24 L3 19" fill="#4f9f5a"/></g>
      <path transform="translate(267 316)" d="M0 -16 C10 -8 10 8 0 16 C-10 8 -10 -8 0 -16Z" fill="#4f9f5a"/>
      <path transform="translate(267 406)" d="M0 12 C-14 6 -16 -6 -10 -12 C-2 -8 0 0 0 12 C0 0 2 -8 10 -12 C16 -6 14 6 0 12Z" fill="#7cbf5a"/>
      <path transform="translate(267 500)" d="M0 -16 C10 -8 10 8 0 16 C-10 8 -10 -8 0 -16Z" fill="#f0bf3a"/>
    </svg>
    <div class="achievement-label">ACHIEVEMENT</div>

    <svg class="magnet-tray" viewBox="0 0 600 160" aria-label="Reward magnets">
      <g stroke="#fff" stroke-width="3">
        <path transform="translate(28 40)" d="M0 -26 C16 -12 16 12 0 26 C-16 12 -16 -12 0 -26Z" fill="#f0bf3a"/>
        <g transform="translate(104 34)"><circle r="18" fill="#f0bf3a"/><path d="M-10 14 L-14 34 L-4 28 M10 14 L14 34 L4 28" fill="#4f9f5a"/></g>
        <path transform="translate(188 36)" d="M0 -24 L5 -5 L24 0 L5 5 L0 24 L-5 5 L-24 0 L-5 -5Z" fill="#f0bf3a"/>
        <g transform="translate(274 32)"><circle r="18" fill="#f0bf3a"/><circle r="10" fill="#2a8fc4"/><path d="M-10 14 L-14 34 L-4 28 M10 14 L14 34 L4 28" fill="#1d8aa6"/></g>
        <path transform="translate(364 38)" d="M0 -22 L4 -4 L22 0 L4 4 L0 22 L-4 4 L-22 0 L-4 -4Z" fill="#2a8fc4"/>
        <g transform="translate(448 32)"><circle r="18" fill="#4f9f5a"/><path d="M-10 14 L-14 34 L-4 28 M10 14 L14 34 L4 28" fill="#3b7d52"/></g>
        <path transform="translate(518 44)" d="M0 -28 C16 -12 16 12 0 28 C-16 12 -16 -12 0 -28Z" fill="#4f9f5a"/>
        <path transform="translate(52 108)" d="M0 22 C-22 14 -26 -4 -16 -14 C-4 -8 0 6 0 22 C0 6 4 -8 16 -14 C26 -4 22 14 0 22Z" fill="#7cbf5a"/>
        <path transform="translate(156 112)" d="M0 -22 L4 -4 L22 0 L4 4 L0 22 L-4 4 L-22 0 L-4 -4Z" fill="#8ccde0"/>
        <path transform="translate(236 106)" d="M0 24 V-20 M0 0 C-12 -2 -14 -14 -10 -18 C-2 -14 0 -8 0 0 M0 0 C12 -2 14 -14 10 -18 C2 -14 0 -8 0 0" fill="#7cbf5a"/>
        <path transform="translate(320 108)" d="M0 22 C-22 14 -26 -4 -16 -14 C-4 -8 0 6 0 22 C0 6 4 -8 16 -14 C26 -4 22 14 0 22Z" fill="#5db6cc"/>
        <path transform="translate(400 104) rotate(45)" d="M0 -26 C16 -12 16 12 0 26 C-16 12 -16 -12 0 -26Z" fill="#4f9f5a"/>
        <g transform="translate(476 98)"><circle r="18" fill="#2a8fc4"/><circle r="9" fill="#f0bf3a"/><path d="M-10 14 L-14 34 L-4 28 M10 14 L14 34 L4 28" fill="#4f9f5a"/></g>
      </g>
    </svg>
  </main>
</body>
</html>
```